Poster Design Project

We are launching a new company Q Vizo, we sell advertising on digital signage and we are launching our company selling ads at our 2 locations, Barlow Heights Sports and Rec Club and the Merrowby Bay Sports and Rec Club. We want to advertise that we have 5 10 and 15 ad slots available and ads start from as little as $27.00 per week. We need to let people know we offer 10% discount to KNBTA members. it needs to have the following contact details to get more information, Marcus 0427359012 and marcus@qvizo.com.au. As a new launch we are offering for the first 10 customers one of 2 discounts, get 4 weeks free all you have to pay is the content creation fee ($99 for 5 second ad) or 4 weeks free and free content creation if you sign up to a 18 week contract.

Update: need the add to start wit something like this but you can be creative:

Need to get you message or brand out, Have you heard of digital sinage?
We have ads avaliable starting from $27 per week at one of our locations.

Or something like that, as i am introducing my company they dont know what i do you untill they read this poster.

Target Market(s)

Targeting small to medium buisness

Industry/Entity Type

Advertising

Requirements
Must have
• Logo

```html
<!DOCTYPE html>
<html lang="en">
<head>
<meta charset="utf-8">
<title>Q Vizo – Digital Signage Poster</title>
<link href="https://fonts.googleapis.com/css2?family=Graduate&family=Patrick+Hand+SC&display=swap" rel="stylesheet">
<style>
  :root {
    --stage: #2a2a2a;
    --paper: #ffffff;
    --mist: #e4e4e4;
    --orange: #f8ae45;
    --blue: #1676c0;
    --green: #3cb54a;
    --grey: #8a8a8a;
    --ink: #111111;
    --white: #ffffff;
  }
  html, body {
    margin: 0;
    width: 1200px;
    height: 1000px;
    overflow: hidden;
    background: var(--stage);
  }
  .poster {
    position: absolute;
    left: 293px;
    top: 67px;
    width: 612px;
    height: 866px;
    background: var(--paper);
    overflow: hidden;
  }
  .poster__shapes {
    position: absolute;
    inset: 0;
  }
  .watermark-name {
    position: absolute;
    left: -40px;
    top: 40px;
    font-family: "Graduate", serif;
    font-size: 190px;
    color: var(--mist);
    transform: rotate(-20deg);
    transform-origin: left top;
    white-space: nowrap;
    opacity: .8;
  }
  .brand {
    position: absolute;
    left: 175px;
    top: 150px;
    display: flex;
    align-items: center;
    gap: 14px;
    transform: rotate(-20deg);
    transform-origin: left center;
  }
  .brand__mark {
    width: 46px;
    height: 46px;
    background: var(--blue);
  }
  .brand__name {
    font-family: "Graduate", serif;
    font-size: 52px;
    color: var(--ink);
    line-height: 1;
  }
  .pitch {
    position: absolute;
    right: 182px;
    top: 262px;
    width: 520px;
    text-align: right;
    transform: rotate(-20deg);
    transform-origin: right top;
    text-transform: uppercase;
  }
  .pitch__headline {
    margin: 0;
    font-family: "Graduate", serif;
    font-size: 25px;
    line-height: 1.05;
    color: var(--blue);
    letter-spacing: 1px;
  }
  .pitch__question {
    margin: 2px 0 4px;
    font-family: "Graduate", serif;
    font-size: 15px;
    color: var(--orange);
    letter-spacing: 1px;
  }
  .pitch__body {
    margin: 0;
    font-family: "Patrick Hand SC", cursive;
    font-size: 19px;
    line-height: 1.15;
    color: var(--grey);
    letter-spacing: 1px;
  }
  .pitch__price { color: var(--blue); }
  .locations {
    margin: 4px -70px 0 0;
    font-family: "Graduate", serif;
    font-size: 17px;
    line-height: 1.15;
    letter-spacing: 1px;
  }
  .locations__count,
  .locations__join {
    font-family: "Patrick Hand SC", cursive;
    font-size: 19px;
    color: var(--ink);
    margin: 0;
  }
  .locations__club {
    color: var(--blue);
    margin: 0;
  }
  .locations__club--far { margin-top: 16px; }
  .offer-band {
    position: absolute;
    left: 0;
    right: 0;
    bottom: 0;
    height: 155px;
    background: var(--blue);
    color: var(--white);
    text-align: center;
    text-transform: uppercase;
    letter-spacing: 1px;
  }
  .offer-band__discount {
    margin: 22px 0 2px;
    font-family: "Graduate", serif;
    font-size: 25px;
  }
  .offer-band__percent {
    font-family: "Patrick Hand SC", cursive;
    font-size: 32px;
  }
  .offer-band__contact {
    margin: 0;
    font-family: "Patrick Hand SC", cursive;
    font-size: 24px;
    line-height: 1.05;
  }
</style>
</head>
<body>
  <main class="poster">
    <svg class="poster__shapes" width="612" height="866" viewBox="0 0 612 866" aria-hidden="true">
      <defs>
        <linearGradient id="mist-fade" x1="0" y1="0" x2="0" y2="1">
          <stop offset="0" stop-color="#d9d9d9"/>
          <stop offset="1" stop-color="#ffffff"/>
        </linearGradient>
      </defs>
      <rect width="612" height="380" fill="url(#mist-fade)"/>
      <polygon points="0,365 487,96 612,650 612,660 442,255 0,383" fill="var(--orange)"/>
      <polygon points="0,383 442,255 612,660 612,866 0,866" fill="var(--paper)"/>
      <polygon points="512,128 552,114 612,350 612,520" fill="var(--blue)"/>
      <polygon points="579,163 612,151 612,268" fill="var(--green)"/>
    </svg>

    <div class="watermark-name" aria-hidden="true">Q Vizo</div>

    <div class="brand">
      <span class="brand__mark"></span>
      <span class="brand__name">Q Vizo</span>
    </div>

    <section class="pitch">
      <h1 class="pitch__headline">Need to get your<br>message or brand out</h1>
      <p class="pitch__question">Have you heard of digital signage ?</p>
      <p class="pitch__body">
        We have ads available starting<br>
        from <span class="pitch__price">$27</span> per week at two of our locations.<br>
        We sell advertising on digital signage and we are<br>
        launching our company selling ads at our
      </p>
      <div class="locations">
        <p class="locations__count">2 locations,</p>
        <p class="locations__club">Barlow Heights Sports<br>and Rec Club</p>
        <p class="locations__join">and</p>
        <p class="locations__club">The Merrowby Bay Sports<br>and Rec Club</p>
      </div>
    </section>

    <footer class="offer-band">
      <p class="offer-band__discount"><span class="offer-band__percent">10%</span> discount to KNBTA members</p>
      <p class="offer-band__contact">For more info contact Marcus:</p>
      <p class="offer-band__contact">042-735-9012 marcus@qvizo.com.au.</p>
    </footer>
  </main>
</body>
</html>
```